Brantley Metal Roofing INC.

Hello,
I am working with a local business to design them a new website. The designer I had worked with moved to colorado and has taken a new job. He recommended that I try posting my new jobs on here. I would need a design and assistance setting the site up on my hostmerry server. I work by myself and handle the sales side of things and need a designer that can help me out.
This company is a metal roofing business. The current page I made for them is www.brantleymetalinc.example

They would like the new site to be similar to http://www.dovecreekalloy.example

Please let me know if this is something that you could do for us.
Updates

the company wants the site to look very similar to this http://www.dovecreekalloy.exampleis that something you could do, please get in touch with me.Thanks Added Tuesday, January 10, 2017

Industry/Entity Type

Business

Font styles to use
Sans Serif

Colors
ed252d

Requirements
Must have
• the company wants the site to look very similar to this
• http://www.dovecreekalloy.example
• is that something you could do, please get in touch with me.
• Thanks

```html
<!DOCTYPE html>
<html lang="en">
<head>
<meta charset="utf-8">
<title>Brantley Metal Inc</title>
<link rel="stylesheet" href="https://fonts.googleapis.com/css2?family=Roboto:wght@400;500;700&family=Roboto+Slab:wght@300;400&family=Raleway:wght@400;500&display=swap">
<style>
:root{
  --red:#ed252d;
  --red-deep:#b8141b;
  --ink:#1d1d1d;
  --text:#555;
  --paper:#f1f1f0;
  --dark:#262626;
  --darker:#111;
  --white:#fff;
}
*{box-sizing:border-box;margin:0;padding:0}
html,body{width:1200px;height:2539px;overflow:hidden}
body{position:relative;background:var(--paper);font-family:"Raleway",sans-serif;color:var(--text)}
.abs{position:absolute}
.wrap{position:absolute;left:149px;width:900px}

/* header */
.site-header{position:absolute;left:0;top:0;width:1200px;height:107px}
.brand{position:absolute;left:149px;top:58px;font:700 21px "Roboto",sans-serif;color:var(--red);letter-spacing:.3px}
.call{position:absolute;left:933px;top:24px;display:flex;gap:6px;align-items:flex-start}
.call small{display:block;font:500 10px "Roboto",sans-serif;color:var(--ink)}
.call strong{display:block;font:700 16px "Roboto",sans-serif;color:var(--red);line-height:16px}
.main-nav{position:absolute;top:81px;left:696px;display:flex;gap:0;font:500 11px "Roboto",sans-serif;color:var(--ink)}
.main-nav a{color:inherit;text-decoration:none;position:absolute;white-space:nowrap}
.main-nav a.active{color:var(--red)}

/* hero */
.hero{position:absolute;left:149px;top:107px;width:900px;height:380px}
.hero-menu{position:absolute;left:0;top:0;width:272px;height:380px;background:var(--dark)}
.hero-menu .item{position:absolute;left:0;width:272px;display:flex;align-items:center;padding-left:16px;gap:12px;border-top:1px solid #3a3a3a;color:var(--white)}
.hero-menu .item.active{background:#444}
.hero-menu .item b{display:block;font:500 16px "Roboto",sans-serif}
.hero-menu .item span{display:block;font:400 10px "Roboto",sans-serif;color:#bbb}
.hero-menu .tab{position:absolute;right:0;top:0;width:30px;height:100%;background:var(--red);display:flex;align-items:center;justify-content:center}
.hero-photo{position:absolute;left:272px;top:0;width:628px;height:380px;background:linear-gradient(160deg,#8fb4dc 0%,#c9d4df 28%,#9a8a74 55%,#5d6a3e 85%,#3f4a2a 100%)}

/* welcome */
.welcome{position:absolute;left:0;top:487px;width:1200px;height:381px;background:var(--white);text-align:center}
.welcome .kicker{position:absolute;left:0;width:100%;top:62px;font:300 22px "Roboto Slab",serif;letter-spacing:2px;color:#444}
.welcome .name{position:absolute;left:0;width:100%;top:106px;font:700 28px "Roboto",sans-serif;color:var(--red)}
.welcome h2{position:absolute;left:0;width:100%;top:160px;font:700 18px "Roboto",sans-serif;color:var(--ink)}
.welcome p{position:absolute;left:150px;width:900px;top:194px;font:400 11.5px/15px "Raleway",sans-serif;color:#666}
.btn{display:inline-flex;align-items:center;justify-content:center;background:var(--red);color:var(--white);font:700 12px "Roboto",sans-serif;letter-spacing:1px;text-transform:uppercase}
.welcome .btn{position:absolute;left:520px;top:268px;width:160px;height:45px;border-radius:23px}

/* services */
.services{position:absolute;left:0;top:868px;width:1200px;height:665px;background:var(--paper)}
.section-title{position:absolute;left:0;width:100%;text-align:center;font:300 28px "Roboto Slab",serif;letter-spacing:1px;color:#333}
.section-title em{font-style:normal;color:var(--red)}
.services .section-title{top:63px}
.services .lede{position:absolute;left:150px;width:900px;top:109px;text-align:center;font:400 11.5px/15px "Raleway",sans-serif;color:#555}
.card{position:absolute;top:191px;width:283px;height:398px;background:var(--white)}
.card .photo{width:100%;height:248px}
.card h3{position:absolute;left:18px;top:267px;font:700 17px "Roboto",sans-serif;color:var(--red);text-transform:uppercase}
.card h4{position:absolute;left:18px;top:290px;font:500 13px "Roboto",sans-serif;color:var(--ink);text-transform:uppercase}
.card p{position:absolute;left:18px;top:318px;width:240px;font:400 11px/15px "Raleway",sans-serif;color:#555}
.card .more{position:absolute;left:18px;top:361px;font:700 12px "Roboto",sans-serif;color:var(--red);display:flex;gap:6px;align-items:center}

/* gallery */
.gallery{position:absolute;left:0;top:1533px;width:1200px;height:545px;background:linear-gradient(180deg,#c0121a 0%,#b3111a 100%)}
.gallery .section-title{top:70px;color:var(--white)}
.g-main{position:absolute;left:152px;top:153px;width:528px;height:318px;border:3px solid var(--red);background:linear-gradient(180deg,#7d92b0 0%,#a7a8ad 30%,#8a5a3a 60%,#6b4026 100%)}
.g-thumb{position:absolute;width:171px;height:152px}
.g-arrows{position:absolute;left:582px;top:488px;display:flex;gap:6px}

/* newsletter */
.newsletter{position:absolute;left:0;top:2078px;width:1200px;height:193px;background:var(--white)}
.newsletter h2{position:absolute;left:149px;top:50px;font:700 27px "Roboto",sans-serif;color:var(--red);letter-spacing:.5px}
.newsletter .sub{position:absolute;left:149px;top:80px;font:500 17px "Roboto",sans-serif;color:#333}
.newsletter .field{position:absolute;left:465px;top:55px;width:432px;height:47px;border:1px solid #999;background:var(--white);font:400 10px "Raleway",sans-serif;color:#777;padding:17px 18px}
.newsletter .btn{position:absolute;left:902px;top:55px;width:147px;height:47px}
.follow{position:absolute;left:149px;top:137px;width:252px;height:56px;background:var(--dark);display:flex;align-items:center;padding-left:30px;gap:14px;color:var(--white);font:500 13px "Roboto",sans-serif}
.follow i{display:inline-block;width:18px;height:18px;border-radius:50%;background:var(--white)}

/* footer */
.site-footer{position:absolute;left:0;top:2271px;width:1200px;height:268px;background:linear-gradient(180deg,#141414,#070707)}
.contact-box{position:absolute;left:149px;top:0;width:252px;height:192px;background:var(--red);color:var(--white);padding:29px 22px}
.contact-box .brand-f{font:700 17px "Roboto",sans-serif}
.contact-box small{display:block;font:400 12px "Raleway",sans-serif;margin-top:22px}
.contact-box small+strong{display:block;font:500 15px "Roboto",sans-serif}
.contact-box strong{font:500 15px "Roboto",sans-serif}
.f-col{position:absolute;top:30px}
.f-col h3{font:500 19px "Roboto",sans-serif;color:var(--red);margin-bottom:14px}
.f-col li{list-style:none;font:400 10.5px/23px "Raleway",sans-serif;color:#ccc}
.f-col li .closed{color:var(--red)}
.f-col li b{color:var(--white);font-weight:500}
.copyright{position:absolute;left:0;width:100%;top:224px;text-align:center;font:400 10px "Raleway",sans-serif;color:#bbb}
.copyright span{color:var(--red)}
</style>
</head>
<body>

<header class="site-header">
  <div class="brand">BRANTLEY METAL INC</div>
  <div class="call">
    <svg width="13" height="22" viewBox="0 0 13 22"><rect x="1" y="1" width="11" height="20" rx="2" fill="#222"/><rect x="3" y="4" width="7" height="11" fill="#fff"/></svg>
    <div><small>Call Now:</small><strong>555-014-0765</strong></div>
  </div>
  <nav class="main-nav">
    <a class="active" style="left:0">Home</a>
    <a style="left:67px">About Us</a>
    <a style="left:150px">Services</a>
    <a style="left:230px">Gallery</a>
    <a style="left:301px">Contact Us</a>
  </nav>
</header>

<section class="hero">
  <div class="hero-menu">
    <div class="item active" style="top:49px;height:81px">
      <svg width="20" height="18" viewBox="0 0 20 18"><path d="M10 1 1 9h3v8h5v-5h2v5h5V9h3z" fill="#fff"/></svg>
      <div><b>Complete Post Frame</b><span>Building Packages</span></div>
      <div class="tab"><svg width="9" height="12" viewBox="0 0 9 12"><path d="M1 0 9 6 1 12z" fill="#fff"/></svg></div>
    </div>
    <div class="item" style="top:130px;height:76px">
      <svg width="20" height="14" viewBox="0 0 20 14"><path d="M2 13 7 2h11l-5 11z" fill="none" stroke="#ccc" stroke-width="1.5"/><path d="M5 8h10M4 11h10" stroke="#ccc"/></svg>
      <div><b>Residential</b><span>Metal Roofing</span></div>
    </div>
    <div class="item" style="top:206px;height:76px">
      <svg width="20" height="20" viewBox="0 0 20 20"><path d="M10 2 2 8v10h16V8z" fill="none" stroke="#fff" stroke-width="1.8"/><rect x="7" y="10" width="6" height="8" fill="#fff"/></svg>
      <div><b>Commercial</b><span>Application</span></div>
    </div>
    <div class="item" style="top:282px;height:98px">
      <svg width="20" height="20" viewBox="0 0 20 20"><path d="M10 2 2 10l8 8 8-8z" fill="none" stroke="#fff" stroke-width="1.8"/><path d="M6 10h8" stroke="#fff" stroke-width="1.8"/></svg>
      <div><b>AGRICULTURAL</b><span>Application</span></div>
    </div>
  </div>
  <div class="hero-photo" role="img" aria-label="Two-storey house with stone chimney and dark metal roof beside an autumn tree"></div>
</section>

<section class="welcome">
  <div class="kicker">WELCOME</div>
  <div class="name">BRANTLEY METAL INC</div>
  <h2>Suspendisse ut rhoncus metus. Morbi accumsan, sem id tincidunt porta</h2>
  <p>Aenean iaculis sit amet augue non imperdiet. Sed viverra in nisl sit amet aliquam. Nam lacinia auctor arcu, et elementum ipsum posuere id. Duis quis pulvinar est, nec tincidunt massa. Proin nisi ante, placerat ac volutpat eu, pulvinar at felis. Nulla tristique eros odio, quis tincidunt massa faucibus ut.</p>
  <span class="btn">Learn More</span>
</section>

<section class="services">
  <h2 class="section-title">OUR <em>SERVICES</em></h2>
  <p class="lede">Nulla facilisi. Fusce eu justo eu magna pulvinar eleifend eu ac nisi. Morbi ut feugiat velit. Integer nec ex aliquam, pharetra ante eget, tempus erat. Vivamus sit amet mollis nisi. Phasellus dignissim sodales malesuada.</p>

  <article class="card" style="left:149px">
    <div class="photo" role="img" aria-label="White farmhouse with balcony below a mountain" style="background:linear-gradient(180deg,#9fb6cf 0%,#d5d7d6 45%,#8d9278 80%,#5c6a45 100%)"></div>
    <h3>Complete Post Frame</h3><h4>Building Packages</h4>
    <p>Call us for a quote, or stop in and we can help you design</p>
    <span class="more">READ MORE <svg width="12" height="10" viewBox="0 0 12 10"><path d="M0 3h6V0l6 5-6 5V7H0z" fill="#222"/></svg></span>
  </article>
  <article class="card" style="left:459px">
    <div class="photo" role="img" aria-label="Modern commercial building with red and white facade under blue sky" style="background:linear-gradient(160deg,#3a86d4 0%,#7fb2e0 40%,#c8493e 70%,#8d8d92 100%)"></div>
    <h3>Commercial</h3><h4>Application</h4>
    <p>Call us for a quote, or stop in and we can help you design</p>
    <span class="more">READ MORE <svg width="12" height="10" viewBox="0 0 12 10"><path d="M0 3h6V0l6 5-6 5V7H0z" fill="#222"/></svg></span>
  </article>
  <article class="card" style="left:767px">
    <div class="photo" role="img" aria-label="Dormer window on a dark tiled roof against blue sky" style="background:linear-gradient(135deg,#2b2b2e 0%,#4a4a4e 40%,#dfe3e6 60%,#6aa6dc 100%)"></div>
    <h3>Residential</h3><h4>Metal Roofing</h4>
    <p>Call us for a quote, or stop in and we can help you design</p>
    <span class="more">READ MORE <svg width="12" height="10" viewBox="0 0 12 10"><path d="M0 3h6V0l6 5-6 5V7H0z" fill="#222"/></svg></span>
  </article>
</section>

<section class="gallery">
  <h2 class="section-title">OUR GALLERY</h2>
  <div class="g-main" role="img" aria-label="Wood-clad modern building with stepped facade and tall glass windows"></div>
  <div class="g-thumb" role="img" aria-label="Dark interior view of a building" style="left:696px;top:153px;background:linear-gradient(180deg,#2a1c1c,#4a3030)"></div>
  <div class="g-thumb" role="img" aria-label="House with red roof on a green lawn" style="left:878px;top:153px;background:linear-gradient(180deg,#5d8fd0 0%,#c58a52 50%,#4e8a35 100%)"></div>
  <div class="g-thumb" role="img" aria-label="Red barn with white trim and lawn" style="left:696px;top:319px;background:linear-gradient(180deg,#7fb3e6 0%,#a33328 55%,#5a9a3e 100%)"></div>
  <div class="g-thumb" role="img" aria-label="Modern apartment building with orange and wood panels" style="left:878px;top:319px;background:linear-gradient(160deg,#5f9ed8 0%,#c2683a 50%,#b8a27a 100%)"></div>
  <div class="g-arrows">
    <svg width="10" height="12" viewBox="0 0 10 12"><path d="M10 0 0 6l10 6z" fill="#f2b6b8"/></svg>
    <svg width="10" height="12" viewBox="0 0 10 12"><path d="M0 0l10 6-10 6z" fill="#f2b6b8"/></svg>
  </div>
</section>

<section class="newsletter">
  <h2>NEWSLETTER</h2>
  <div class="sub">Subscribes Your Newsletter</div>
  <div class="field">Enter Your Email:</div>
  <span class="btn">Subscribe</span>
  <div class="follow">Follow Us: <i></i><i></i><i></i></div>
</section>

<footer class="site-footer">
  <div class="contact-box">
    <div class="brand-f">BRANTLEY METAL INC</div>
    <small>Phone:</small><strong>555-014-0765</strong>
    <small>Fax:</small><strong>555-014-4931</strong>
  </div>
  <div class="f-col" style="left:516px">
    <h3>Sitemap</h3>
    <ul><li>Home</li><li>About Us</li><li>Services</li><li>Gallery</li><li>Contact Us</li></ul>
  </div>
  <div class="f-col" style="left:728px">
    <h3>Services</h3>
    <ul><li>Residential</li><li>Commercial</li><li>Agricultural</li><li>Complete Project</li></ul>
  </div>
  <div class="f-col" style="left:921px">
    <h3>Hours</h3>
    <ul><li>Monday - Friday: 7am - 5pm</li><li>Saturday: 7AM-12PM</li><li><b>Sunday:</b> <span class="closed">Closed</span></li></ul>
  </div>
  <div class="copyright">Copyright © 2017 <span>Brantley Metal Inc</span>. All rights reserved.</div>
</footer>

</body>
</html>
```